Kelvoranet.com Webpage Design

Design Brief for kelvoranet.com (Copy of Brief also in attached Word file)

Name of Website- kelvoranet.com (existing logo and look & feel of website to be changed)

Logo - Finalised. The logo files are attached with the brief as “logo.jpeg”. The “Blue- Grey” version of the logo is for use on lighter backgrounds and the “Orange-White” version of the logo is for use on darker backgrounds. (A full Black version of the logo is also attached). Both versions may be used in different parts of the website. All attached files are in .png format.
Status - The website in functional and is undergoing user trials. However, we want to improve the look & feel of the website so at it seems
a. cotemporary,
b. Easy to Navigate
c. professional and
d. Vibrant.

Please visit ‘kelvoranet.com’ to check out the website and its functionalities – please use it only as a reference for the features & functions to be provided, however the designer should use a ‘Free Hand’ in designing the composition of various parts of the webpage without getting too influenced by the existing design

Objective of the Website ‘kelvoranet.com –
a. It is a portal focussed on listing of ‘Retail’ specific real-estate properties by developers, owners and realty brokers. The properties shall listed under the following four categories-
i. Retail Malls
ii. Shopping Complexes
iii. High-street shops
iv. Retail Warehouses
*refer kelvoranet.com for better clarity

b. The abovementioned properties shall be listed either for ‘Sale’ or ‘rent\lease’ or both

c. Users shall visit the site in case they wish to acquire a retail \ shop space either on ‘sale’ or ‘rent’. These Users would be able to specify the ‘Search Criteria’ through the tool-bars provided on the website – the ‘Search Criteria’ shall comprise of ‘Type of space category’, ‘City’, ‘Locality’, transaction type ie ‘Rent \ Sale’ and ‘Area Range’

d. The main revenue model for the website shall be listing fee ( or advertising charges ) payable by those listing their properties on the website.

Three Main Pages of Website (kelvoranet.com) that need to be designed -
a. Main Home Page (visit the web link - http://kelvoranet.com/ ) - The main home page has the “Search Toolbar” for specifying of Search Criteria by the User. It shall also have the following features & functions-
i. Main Advertising Banner
ii. Featured Projects
iii. New Launches
iv. Toolbar with buttons – ‘Advertise with Us’, ‘Listings Alert’, ‘Quorra Desk’, ‘Advertiser Login’

b. Property Listings Page (visit the web link - http://kelvoranet.com/gurgaon-in-india ) - The List of property options that match the Criteria specified by the ‘User’ get displayed on this page.

c. Property Detail Page - When the ‘User’ clicks on the “More….” Button on the ‘Property Listings Page’ (given in point b. above) the web page with the details of the property opens. (For Example – visit the web link - http://kelvoranet.com/dorvik-Shopping-Complex-dorvik-bellmoor-gurgaon-636 )

Note:- Please refer to attached ‘Shopping’ related images the designer may use them on the website to provide a look & feel of retail if required – either separately or rotate in a single window

Target Market(s)

Retailers & Investors looking for retail space, Real Estate Brokers, Developers

Industry/Entity Type

Advertising

Number of Pages Required

3 page

Requirements
Must have
• Refer to existing site kelvoranet.com -- all the existing functionalities are a must have.
Nice to have
• The Designer may use the retail related images on the website if required for making it more vibrant. Refer attached images Shopping(1-6).jpg

```html
<!DOCTYPE html>
<html lang="en">
<head>
<meta charset="utf-8">
<title>Kelvoranet.com – Retail Space Portal</title>
<link href="https://fonts.googleapis.com/css2?family=Open+Sans:wght@400;600;700&display=swap" rel="stylesheet">
<style>
:root{
  --blue:#1e88d8;
  --blue-dark:#0f4f86;
  --navy:#0b2c4a;
  --navy-deep:#071d33;
  --orange:#f37021;
  --grey-bg:#f1f3f5;
  --grey-line:#d8dde2;
  --text:#333a40;
  --muted:#7a848d;
  --white:#ffffff;
}
*{box-sizing:border-box;margin:0;padding:0}
html,body{width:1200px;height:2416px;overflow:hidden}
body{font-family:"Open Sans",Arial,sans-serif;color:var(--text);background:var(--white);font-size:12px}
.wrap{width:1000px;margin:0 auto;position:relative}
.topbar{height:18px;background:var(--grey-bg);border-bottom:1px solid var(--grey-line);font-size:9px;color:var(--muted)}
.topbar .wrap{display:flex;gap:14px;line-height:18px}
.header{height:82px}
.header .wrap{display:flex;align-items:center;height:82px}
.brand{display:flex;align-items:center;gap:8px;font-weight:700;font-size:26px;color:var(--blue-dark)}
.brand .dot{width:22px;height:22px;border-radius:50%;background:var(--orange)}
.header-contact{margin-left:auto;display:flex;gap:26px;align-items:center;font-size:12px;color:var(--muted)}
.header-contact span{display:flex;align-items:center;gap:6px}
.btn{display:inline-block;border:0;font-family:inherit;font-weight:600;color:var(--white);cursor:pointer}
.btn-orange{background:var(--orange)}
.btn-blue{background:var(--blue)}
.list-btn{padding:9px 16px;font-size:12px;border-radius:2px}
.nav{height:32px;background:var(--blue)}
.nav .wrap{display:flex;align-items:center;height:32px;gap:30px;color:var(--white);font-size:12px;font-weight:600}
.nav .lang{margin-left:auto;background:var(--white);color:var(--text);font-weight:400;font-size:10px;width:110px;height:20px;line-height:20px;padding:0 8px}
.hero{height:460px;background:linear-gradient(100deg,#0b0d14 0%,#1a1f30 40%,#3a3040 65%,#6a4a3c 100%);position:relative}
.hero .wrap{height:460px}
.hero-copy{position:absolute;top:130px;left:0;width:460px;color:var(--white)}
.hero-copy h1{font-size:34px;font-weight:700;line-height:1.25}
.hero-copy h1 em{font-style:normal;color:var(--blue)}
.hero-copy p{font-size:11px;line-height:1.5;margin:12px 0 18px;color:#d6dbe0}
.hero-copy .btn{padding:9px 18px;font-size:12px}
.hero-arrow{position:absolute;top:210px;width:26px;height:40px;background:rgba(255,255,255,.15);color:var(--white);text-align:center;line-height:40px;font-size:18px}
.search{height:96px;background:var(--blue)}
.search .wrap{padding-top:10px;color:var(--white)}
.search-row{display:flex;gap:10px;align-items:flex-end}
.field{flex:1}
.field label{display:block;font-size:9px;margin-bottom:3px}
.field .input{height:24px;background:var(--white);font-size:10px;color:var(--muted);padding:0 8px;line-height:24px}
.search-row .btn{width:110px;height:24px;font-size:13px;text-align:center;line-height:24px}
.checks{display:flex;gap:22px;margin-top:12px;font-size:10px}
.checks span{display:flex;align-items:center;gap:5px}
.checks i{width:10px;height:10px;background:var(--white);display:inline-block}
.formats{height:112px;border-bottom:1px solid var(--grey-line)}
.formats .wrap{display:flex;gap:40px;padding:22px 40px 0}
.format{flex:1;display:flex;gap:10px}
.format h3{font-size:12px;color:var(--blue-dark);font-weight:700}
.format p{font-size:9px;color:var(--muted);line-height:1.45;margin-top:3px}
.section-title{font-size:22px;font-weight:600;color:var(--text);display:flex;align-items:baseline;gap:8px}
.section-title small{font-size:9px;color:var(--muted);font-weight:400}
.featured{padding:40px 0 0;height:380px}
.cards{display:flex;gap:16px;margin-top:22px}
.card{width:187px;background:var(--white);border:1px solid var(--grey-line)}
.card .photo{height:140px;background:linear-gradient(180deg,#8fc3ea,#c9d3db 70%,#9aa6ae);position:relative}
.card .tag{position:absolute;right:0;bottom:0;background:var(--white);font-size:9px;padding:2px 8px;color:var(--text)}
.card .info{padding:10px 10px 8px}
.card h4{font-size:13px;color:var(--blue-dark)}
.card .meta{display:flex;justify-content:space-between;font-size:9px;color:var(--muted);margin-top:4px}
.card .btn{display:block;width:100%;text-align:center;height:28px;line-height:28px;font-size:11px}
.side-arrow{position:absolute;top:180px;font-size:24px;color:var(--muted)}
.launches{height:390px;background:linear-gradient(180deg,var(--navy) 0%,var(--navy-deep) 100%);padding-top:40px}
.launches .section-title{color:var(--white)}
.launches .side-arrow{top:180px;background:var(--blue);color:var(--white);width:22px;height:40px;line-height:38px;text-align:center;font-size:18px}
.trio{height:430px;padding-top:40px}
.trio .wrap{display:flex;gap:40px}
.col{flex:1}
.col h3{font-size:18px;font-weight:600;padding-bottom:8px;border-bottom:1px solid var(--grey-line);margin-bottom:12px}
.col p{font-size:10px;line-height:1.5;color:var(--muted)}
.col .input{height:26px;border:1px solid var(--grey-line);font-size:10px;color:var(--muted);padding:0 8px;line-height:24px;margin-top:8px}
.col .input.tall{height:56px}
.col .btn{padding:8px 18px;font-size:11px;margin-top:12px}
.editor{display:flex;gap:12px}
.editor .photo{width:120px;height:140px;flex:none;background:linear-gradient(180deg,#7fb5de,#b8c3cc)}
.footer{height:360px;background:var(--navy-deep);color:#b9c4ce}
.footer .wrap{display:flex;gap:36px;padding-top:34px}
.footer h3{color:var(--white);font-size:15px;font-weight:600;margin-bottom:14px}
.f-col{flex:1;font-size:10px;line-height:1.6}
.thumbs{display:flex;flex-direction:column;gap:10px}
.thumb{display:flex;gap:8px}
.thumb i{width:46px;height:36px;background:linear-gradient(180deg,#5d8fb8,#34506a);flex:none}
.contact-line{display:flex;gap:10px;margin-bottom:10px}
.contact-line b{color:var(--white);font-weight:600;width:56px;flex:none}
.links{list-style:none}
.f-col .input{height:24px;background:#11304d;border:1px solid #1e4466;margin-bottom:8px;padding:0 8px;line-height:22px;color:#7d8f9f}
.f-col .input.tall{height:56px}
.f-col .btn{float:right;padding:7px 22px;font-size:11px}
.bottom{height:56px;background:#05152a;color:#7d8f9f;font-size:10px}
.bottom .wrap{display:flex;align-items:center;height:56px}
.socials{margin-left:auto;display:flex;gap:8px}
.socials i{width:18px;height:18px;border-radius:50%;background:#2a4866;display:block}
</style>
</head>
<body>
<div class="topbar"><div class="wrap"><span>Retail Malls</span><span>Shopping Complexes</span><span>High Street Shops</span><span>Retail Warehouses</span><span>New Launches</span><span>Listing Alerts</span></div></div>

<header class="header"><div class="wrap">
  <div class="brand"><span class="dot"></span>Kelvoranet.com</div>
  <div class="header-contact">
    <span><svg width="14" height="10" viewBox="0 0 14 10"><rect x=".5" y=".5" width="13" height="9" fill="none" stroke="#7a848d"/><path d="M.5 .5 7 6 13.5 .5" fill="none" stroke="#7a848d"/></svg>info@kelvoranet.com</span>
    <span><svg width="12" height="12" viewBox="0 0 12 12"><path d="M2 1h3l1 3-2 1a7 7 0 0 0 3 3l1-2 3 1v3c-6 1-10-3-9-9z" fill="#7a848d"/></svg>555-014-2290</span>
    <a class="btn btn-orange list-btn">List your Property</a>
  </div>
</div></header>

<nav class="nav"><div class="wrap"><span>Home ▾</span><span>Properties ▾</span><span>Features ▾</span><span>Contact us</span><span class="lang">English ▾</span></div></nav>

<section class="hero" role="img" aria-label="Shopper holding shopping bags in a lit mall at night">
  <div class="wrap">
    <div class="hero-copy">
      <h1>Solvane Market <em>Walk</em><br>Gurgaon</h1>
      <p>Premium retail frontage on a busy corridor with strong footfall, wide store fronts, ample parking and flexible sizes for brands, investors and first time retailers alike.</p>
      <a class="btn btn-orange">More Detail</a>
    </div>
  </div>
  <span class="hero-arrow" style="left:0">‹</span><span class="hero-arrow" style="right:0">›</span>
</section>

<section class="search"><div class="wrap">
  <div class="search-row">
    <div class="field"><label>Sale Or Rent Or Both</label><div class="input">Both ▾</div></div>
    <div class="field"><label>Select City</label><div class="input">Gurgaon ▾</div></div>
    <div class="field"><label>Select Locality - Metro - Market</label><div class="input">Select Locality ▾</div></div>
    <div class="field"><label>Enter Keywords</label><div class="input">Name of Project, Developer etc</div></div>
    <a class="btn btn-orange">SEARCH</a>
  </div>
  <div class="checks"><span><i></i>Retail Malls</span><span><i></i>Retail Warehouses</span><span><i></i>Shopping Complexes</span><span><i></i>High Street Shops</span><span>Select Retail Format (Multiple Selections)</span></div>
</div></section>

<section class="formats"><div class="wrap">
  <div class="format"><svg width="26" height="26" viewBox="0 0 26 26"><rect x="3" y="9" width="20" height="14" fill="none" stroke="#1e88d8" stroke-width="2"/><path d="M1 10 13 3l12 7" fill="none" stroke="#1e88d8" stroke-width="2"/></svg><div><h3>Retail Malls</h3><p>Centrally air conditioned malls with anchor stores, food courts and steady weekend crowds.</p></div></div>
  <div class="format"><svg width="26" height="26" viewBox="0 0 26 26"><path d="M5 9h16l-2 14H7z" fill="none" stroke="#f37021" stroke-width="2"/><path d="M9 9V6a4 4 0 0 1 8 0v3" fill="none" stroke="#f37021" stroke-width="2"/></svg><div><h3>Shopping Complex</h3><p>Non air conditioned buildings with shops on many floors and easy access from the road.</p></div></div>
  <div class="format"><svg width="26" height="26" viewBox="0 0 26 26"><rect x="3" y="5" width="20" height="18" fill="none" stroke="#1e88d8" stroke-width="2"/><path d="M3 11h20M11 23v-7h4v7" fill="none" stroke="#1e88d8" stroke-width="2"/></svg><div><h3>High Street Shops</h3><p>Road facing shops in busy markets with strong visibility and daily local footfall.</p></div></div>
</div></section>

<section class="featured"><div class="wrap">
  <h2 class="section-title">Featured Retail Projects <small>Across India</small></h2>
  <div class="cards">
    <div class="card"><div class="photo" role="img" aria-label="Retail tower exterior"><span class="tag">Gurgaon</span></div><div class="info"><h4>Halden Plaza</h4><div class="meta"><span>Gurgaon</span><span>Shopping Complex</span></div></div><a class="btn btn-blue">View the listing</a></div>
    <div class="card"><div class="photo" role="img" aria-label="Retail tower exterior"><span class="tag">Faridabad</span></div><div class="info"><h4>Orla Row Arcade</h4><div class="meta"><span>Gurgaon</span><span>Shopping Complex</span></div></div><a class="btn btn-blue">View the listing</a></div>
    <div class="card"><div class="photo" role="img" aria-label="Retail tower exterior"><span class="tag">Gurgaon</span></div><div class="info"><h4>Kestrel Square</h4><div class="meta"><span>Gurgaon</span><span>Shopping Complex</span></div></div><a class="btn btn-blue">View the listing</a></div>
    <div class="card"><div class="photo" role="img" aria-label="Retail tower exterior"><span class="tag">Gurgaon</span></div><div class="info"><h4>Vesta Court</h4><div class="meta"><span>Gurgaon</span><span>Shopping Complex</span></div></div><a class="btn btn-blue">View the listing</a></div>
    <div class="card"><div class="photo" role="img" aria-label="Retail tower exterior"><span class="tag">Gurgaon</span></div><div class="info"><h4>Halden Plaza</h4><div class="meta"><span>Gurgaon</span><span>Shopping Complex</span></div></div><a class="btn btn-blue">View the listing</a></div>
  </div>
  <span class="side-arrow" style="left:-34px">‹</span><span class="side-arrow" style="right:-34px">›</span>
</div></section>

<section class="launches"><div class="wrap">
  <h2 class="section-title">Featured New Launches <small>Across India</small></h2>
  <div class="cards">
    <div class="card"><div class="photo" role="img" aria-label="New retail building exterior"><span class="tag">Gurgaon</span></div><div class="info"><h4>Halden Plaza</h4><div class="meta"><span>Gurgaon</span><span>Shopping Complex</span></div></div><a class="btn btn-blue">View the listing</a></div>
    <div class="card"><div class="photo" role="img" aria-label="New retail building exterior"><span class="tag">Faridabad</span></div><div class="info"><h4>Orla Row Arcade</h4><div class="meta"><span>Gurgaon</span><span>Shopping Complex</span></div></div><a class="btn btn-blue">View the listing</a></div>
    <div class="card"><div class="photo" role="img" aria-label="New retail building exterior"><span class="tag">Gurgaon</span></div><div class="info"><h4>Kestrel Square</h4><div class="meta"><span>Gurgaon</span><span>Shopping Complex</span></div></div><a class="btn btn-blue">View the listing</a></div>
    <div class="card"><div class="photo" role="img" aria-label="New retail building exterior"><span class="tag">Gurgaon</span></div><div class="info"><h4>Vesta Court</h4><div class="meta"><span>Gurgaon</span><span>Shopping Complex</span></div></div><a class="btn btn-blue">View the listing</a></div>
    <div class="card"><div class="photo" role="img" aria-label="New retail building exterior"><span class="tag">Gurgaon</span></div><div class="info"><h4>Halden Plaza</h4><div class="meta"><span>Gurgaon</span><span>Shopping Complex</span></div></div><a class="btn btn-blue">View the listing</a></div>
  </div>
  <span class="side-arrow" style="left:-48px">‹</span><span class="side-arrow" style="right:-48px">›</span>
</div></section>

<section class="trio"><div class="wrap">
  <div class="col">
    <h3>Listing Alert</h3>
    <p>Subscribe to get fresh retail listings on email, matched to the criteria you set below.</p>
    <div class="input">Enter your email address</div>
    <div class="input">Select option ▾</div>
    <div class="input">Select retail format ▾</div>
    <div class="input">Individual ▾</div>
    <div class="input">Select area of interest ▾</div>
    <a class="btn btn-blue">Subscribe</a>
  </div>
  <div class="col">
    <h3>Editor's Choice</h3>
    <div class="editor">
      <div class="photo" role="img" aria-label="Featured retail project exterior"></div>
      <p>A select listing of retail properties handpicked by our editorial team after a close study of location, footfall, pricing, layout and the track record of the developer. Each pick is reviewed on site before it is shown here, so investors and retailers can shortlist with confidence.</p>
    </div>
    <a class="btn btn-blue" style="float:right">Read More</a>
  </div>
  <div class="col">
    <h3>Quorra Desk</h3>
    <p>Post your retail space need with us and our experts will get back with options that suit your plans.</p>
    <div class="input">Enter your email address</div>
    <div class="input">Your mobile no.</div>
    <div class="input tall">Brief description of requirement</div>
    <a class="btn btn-blue" style="float:right">Read More</a>
  </div>
</div></section>

<footer class="footer"><div class="wrap">
  <div class="f-col"><h3>Featured</h3>
    <div class="thumbs">
      <div class="thumb"><i role="img" aria-label="Project thumbnail"></i><span>Halden Plaza, Gurgaon<br>Shopping Complex</span></div>
      <div class="thumb"><i role="img" aria-label="Project thumbnail"></i><span>Vesta Court, Gurgaon<br>High Street Shops</span></div>
      <div class="thumb"><i role="img" aria-label="Project thumbnail"></i><span>Orla Row, Faridabad<br>Retail Mall</span></div>
    </div>
  </div>
  <div class="f-col"><h3>Contact Us</h3>
    <div class="contact-line"><b>Address</b><span>Sector 14 Market Road,<br>Gurgaon, Haryana</span></div>
    <div class="contact-line"><b>Phone</b><span>555-014-2290</span></div>
    <div class="contact-line"><b>Email</b><span>info@kelvoranet.com</span></div>
    <div class="contact-line"><b>Web</b><span>www.kelvoranet.com</span></div>
  </div>
  <div class="f-col"><h3>About Kelvora Retail</h3>
    <ul class="links"><li>About Us</li><li>Privacy Policy</li><li>Terms of Use</li><li>Contact Us</li><li>Site Map</li><li>Retail Malls</li><li>Shopping Complex</li><li>High Street Shops</li><li>Retail Warehouses</li></ul>
  </div>
  <div class="f-col"><h3>Say Hello!</h3>
    <div class="input">Name</div>
    <div class="input">Email</div>
    <div class="input tall">Message</div>
    <a class="btn btn-blue">Send</a>
  </div>
</div></footer>

<div class="bottom"><div class="wrap">
  <span>Copyright © 2015 Kelvoranet.com. All rights reserved.</span>
  <div class="socials"><i></i><i></i><i></i><i></i><i></i><i></i></div>
</div></div>
</body>
</html>
```